Vital Spark Electrical in need of a business card design

We need a new business card designed for our electrical business. We have a logo already which I will attach below.
Would like the business card to be..
-BLACK background preferably, possibly white back ground behind logo if colours clash.
-White & Blue (logo blue) text
Something that makes the logo pop, & a modern look. Possibly minimal clean format.

REQUIRE:
-Logo on front & back

TEXT TO INCLUDE (ON ONE SIDE):

Tom Harlow
Director/Electrician
M: 0417 365 208
E:info@vitalsparkelectrical-example.com.au
W:www.vitalsparkelectrical-example.com.au
R.E.C 57318

Custom/New Homes
Renovations
Commercial Office/Shop Fit-outs
Communications & Security Cameras
Electric Vehicle Chargers
Airconditioning
Updates

Requirements
Nice to have
• Possibly even lighten the grey shades for the words 'Vital' & 'Spark' to be more easily read on a black background.

```html
<!DOCTYPE html>
<html lang="en">
<head>
<meta charset="utf-8">
<title>Vital Spark Electrical – Business Card</title>
<link href="https://fonts.googleapis.com/css2?family=Roboto:wght@300;400;500&display=swap" rel="stylesheet">
<style>
  :root {
    --navy: #1f3047;
    --cyan: #33dcfb;
    --white: #ffffff;
    --backdrop: #c6d0d1;
    --ink: #1f3047;
  }
  * { box-sizing: border-box; margin: 0; padding: 0; }
  html, body {
    width: 1200px; height: 1200px; overflow: hidden;
    background: var(--backdrop);
    font-family: "Roboto", Arial, sans-serif;
  }
  .canvas { position: relative; width: 1200px; height: 1200px; }

  .card {
    position: absolute; left: 257px; width: 685px; height: 388px;
    background: var(--white); border-radius: 16px; overflow: hidden;
  }
  .card--front { top: 174px; }
  .card--back { top: 634px; }

  /* Front */
  .front-body {
    position: absolute; left: 0; top: 0; width: 100%; height: 310px;
    background: var(--navy);
  }
  .side-tab {
    position: absolute; top: 0; width: 39px; height: 310px; background: var(--cyan);
  }
  .side-tab--left { left: 0; border-radius: 0 30px 30px 0; }
  .side-tab--right { right: 0; border-radius: 30px 0 0 30px; }

  .services {
    position: absolute; left: 172px; top: 86px; list-style: none;
    color: var(--white); font-weight: 400; font-size: 21px; line-height: 24.4px;
    letter-spacing: 0.4px;
  }
  .services li { position: relative; padding-left: 22px; }
  .services li::before {
    content: ""; position: absolute; left: 0; top: 5px;
    width: 15px; height: 15px; border-radius: 50%; background: var(--cyan);
  }

  .brand-mark {
    position: absolute; display: flex; align-items: center; gap: 8px;
    color: var(--ink); font-weight: 500; white-space: nowrap;
  }
  .brand-mark__square { display: block; background: var(--cyan); }
  .front-brand { left: 16px; top: 333px; font-size: 17px; }
  .front-brand .brand-mark__square { width: 16px; height: 16px; }

  .web-bar {
    position: absolute; left: 257px; top: 319px; width: 428px; height: 52px;
    background: var(--cyan); color: var(--white);
    display: flex; align-items: center; padding-left: 14px;
    font-size: 18.5px; font-weight: 400; letter-spacing: 0.2px; white-space: nowrap;
  }

  /* Back */
  .person {
    position: absolute; left: 36px; top: 36px; color: var(--ink);
  }
  .person__name { font-size: 29px; font-weight: 400; letter-spacing: 0.5px; line-height: 1; }
  .person__role { font-size: 18px; font-weight: 400; margin-top: 5px; }

  .back-brand { right: 22px; top: 48px; font-size: 27px; }
  .back-brand .brand-mark__square { width: 24px; height: 24px; }

  .contact-panel {
    position: absolute; left: 215px; top: 182px; width: 470px; height: 170px;
    background: var(--navy); overflow: hidden;
  }
  .panel-tab {
    position: absolute; top: 0; height: 100%; background: var(--cyan);
  }
  .panel-tab--left { left: 0; width: 40px; border-radius: 0 26px 26px 0; }
  .panel-tab--right { right: 0; width: 39px; border-radius: 26px 0 0 26px; }

  .contact-line {
    position: absolute; left: 75px; transform: translateY(-50%);
    color: var(--white); font-size: 19px; font-weight: 400; white-space: nowrap;
  }
  .contact-line--phone { top: 50px; }
  .contact-line--email { top: 97px; font-size: 15.6px; }
  .contact-line--licence { top: 144px; }

  .contact-badge {
    position: absolute; left: 22px; width: 40px; height: 40px; margin-top: -20px;
    border-radius: 50%; background: var(--navy);
    box-shadow: 0 0 0 2px rgba(255,255,255,0.12);
    color: var(--white); font-size: 22px; font-weight: 400;
    display: flex; align-items: center; justify-content: center;
  }
  .contact-badge--phone { top: 46px; }
  .contact-badge--email { top: 96px; }
</style>
</head>
<body>
<div class="canvas">

  <section class="card card--front" aria-label="Business card front">
    <div class="front-body">
      <span class="side-tab side-tab--left"></span>
      <span class="side-tab side-tab--right"></span>
      <ul class="services">
        <li>Custom/New Homes</li>
        <li>Renovations</li>
        <li>Commercial Office/Shop Fit-outs</li>
        <li>Communications &amp; Security Cameras</li>
        <li>Electric Vehicle Chargers</li>
        <li>Airconditioning</li>
      </ul>
    </div>
    <div class="brand-mark front-brand">
      <span class="brand-mark__square"></span>
      <span class="brand-mark__name">Vital Spark Electrical</span>
    </div>
    <div class="web-bar">www.vitalsparkelectrical-example.com.au</div>
  </section>

  <section class="card card--back" aria-label="Business card back">
    <div class="person">
      <p class="person__name">TOM HARLOW</p>
      <p class="person__role">Director/Electrician</p>
    </div>
    <div class="brand-mark back-brand">
      <span class="brand-mark__square"></span>
      <span class="brand-mark__name">Vital Spark Electrical</span>
    </div>

    <div class="contact-panel">
      <span class="panel-tab panel-tab--left"></span>
      <span class="panel-tab panel-tab--right"></span>
      <span class="contact-badge contact-badge--phone">M</span>
      <span class="contact-badge contact-badge--email">E</span>
      <p class="contact-line contact-line--phone">0417 365 208</p>
      <p class="contact-line contact-line--email">info@vitalsparkelectrical-example.com.au</p>
      <p class="contact-line contact-line--licence">R.E.C 57318</p>
    </div>
  </section>

</div>
</body>
</html>
```